Paw Summit Co business card

I need a business card design for a dog training company in Toronto called Paw Summit Co. My training is unique, outdoor training that helps people create a better bond with their dog through communication and understanding their dog's true nature. I do not use treats - but communication and praise for the dog.

I help people create a better life for them and their dog. From puppy training right through to seniors, I offer both group classes called Curbside Poise Course as well as in-home private sessions.

I believe that having a dog is a lifestyle, so I encourage clients to incorporate their dog into their active life. Outdoor activities such as hiking, mental stimulation, proper care and healthy food for their dog are all keys to a healthy and happy dog.

I would like a fresh and modern look that works with my logo. I would like to convey fun, confidence and happiness.

My services are premium services. I am a Certified Dog Trainer, and offer value for money, but my prices are higher than other trainers.
Updates

Thank you to everyone who submitted designs! I'm so impressed with the level of creativity and the options that you all have given me. It will be a difficult choice for sure. As this was my first experience with Art Huddle - it has been a great one.

maren.

Industry/Entity Type

Communication

Requirements
Must have
• Maren Quill, CTE
Certified Trainer Educator
maren@pawsummitco.ca
555-318-0472
pawsummitco.ca

Prefer a double sided card.
Must have Paw Summit Co logo. File attached. I do have a stroke logo for a dark background as well.

Must only use the fonts and colours as outlined in my brand guidelines, which are attached.
Should not have
• no cheesy pet images
do not use the tongue as an element outside of the logo
minimize the use of pink - can be used as an accent colour but should not be a main colour

```html
<!DOCTYPE html>
<html lang="en">
<head>
<meta charset="utf-8">
<title>Paw Summit Co business card</title>
<link rel="stylesheet" href="https://fonts.googleapis.com/css2?family=Noto+Serif:wght@400;700&display=swap">
<style>
  :root {
    --bg: #d6d6d6;
    --dark: #2a2616;
    --pink: #ff2457;
    --green: #8fe21c;
    --white: #ffffff;
    --serif: "Noto Serif", "Times New Roman", serif;
  }
  html, body {
    margin: 0;
    padding: 0;
    width: 1200px;
    height: 1194px;
    overflow: hidden;
    background: var(--bg);
  }
  .canvas {
    position: relative;
    width: 1200px;
    height: 1194px;
  }
  .card {
    position: absolute;
    width: 837px;
    height: 479px;
    overflow: hidden;
  }
  .card-front {
    left: 49px;
    top: 95px;
    background: var(--dark);
  }
  .brand-panel {
    position: absolute;
    left: 0;
    top: 70px;
    width: 698px;
    height: 337px;
    box-sizing: border-box;
    background: var(--green);
    border: 9px solid var(--dark);
    outline: 4px solid var(--pink);
    outline-offset: -13px;
    display: flex;
    align-items: center;
    padding-left: 44px;
    gap: 20px;
  }
  .brand-mark {
    width: 56px;
    height: 56px;
    border-radius: 50%;
    background: var(--pink);
    flex: none;
  }
  .brand-name {
    font-family: var(--serif);
    font-weight: 700;
    font-size: 68px;
    line-height: 1;
    color: var(--dark);
    white-space: nowrap;
  }
  .card-back {
    left: 270px;
    top: 640px;
    background: var(--green);
  }
  .contact-panel {
    position: absolute;
    left: 34px;
    top: 66px;
    width: 704px;
    height: 352px;
    box-sizing: border-box;
    background: var(--dark);
    border: 9px solid var(--pink);
    display: flex;
    flex-direction: column;
    justify-content: center;
    align-items: flex-end;
    padding-right: 40px;
    font-family: var(--serif);
    color: var(--white);
    text-align: right;
    white-space: nowrap;
  }
  .contact-name {
    font-size: 50px;
    line-height: 1.1;
    margin: 0 0 4px;
    font-weight: 400;
  }
  .contact-name .credential {
    font-size: 32px;
  }
  .contact-line {
    font-size: 32px;
    line-height: 1.18;
    margin: 0;
  }
</style>
</head>
<body>
<div class="canvas">
  <section class="card card-front">
    <div class="brand-panel">
      <span class="brand-mark"></span>
      <span class="brand-name">Paw Summit Co</span>
    </div>
  </section>

  <section class="card card-back">
    <div class="contact-panel">
      <h1 class="contact-name">Maren Quill,<span class="credential">CTE</span></h1>
      <p class="contact-line">Certified Trainer Educator</p>
      <p class="contact-line">Pawsummitco.ca</p>
      <p class="contact-line">maren@pawsummitco.ca</p>
      <p class="contact-line">555.318.0472</p>
    </div>
  </section>
</div>
</body>
</html>
```